Membership card Design

Hi I need a new membership card design for a social University club located in New Zealand. Our club name is called Maple Lantern Circle (MLCIR) and we provide a social hub for international students from Asia to meet local students. We are a non-profit organization that organizes activities such as paintball, ski trips, parties and day trips for our members. We need designs that look more like a membership card than a name card because we will be giving them to our members as a proof of membership. We would prefer a design that is simple in the front and with our club details, contacts and a place to write down a membership number on the back. We would like our card to have designs using the colours red, black, grey and orange. The design must incoporate the logo attached in this project. If possible, we would like the flower in the Hong Kong Flag to be incoporated in the design. The final design must look more like a membership card than a name card and communicate professionalism and high quality.
Updates

Target Market(s)

University Students

Industry/Entity Type

Non-Profit

Requirements
Must have
• The design must include:

The logo of our club
Our facebook page details: www.friendspage.example/maplelantern.cir
Our email: maplelanterncir@mailbox.example
A place behind the card to print membership numbers.

```html
<!DOCTYPE html>
<html lang="en">
<head>
<meta charset="utf-8">
<title>Maple Lantern Circle – Membership Card</title>
<link rel="stylesheet" href="https://fonts.googleapis.com/css2?family=EB+Garamond:wght@400;500&display=swap">
<style>
  :root {
    --ink: #000000;
    --paper: #ffffff;
    --club-red: #e8231b;
    --emblem-red: #e1251b;
    --emblem-deep: #c81a12;
    --serif: "EB Garamond", Georgia, serif;
  }
  html, body {
    margin: 0;
    padding: 0;
    width: 1200px;
    height: 965px;
    overflow: hidden;
    background: var(--paper);
    font-family: var(--serif);
  }
  .sheet {
    position: relative;
    width: 1200px;
    height: 965px;
  }

  /* Card front */
  .card-front {
    position: absolute;
    left: 74px;
    top: 42px;
    width: 700px;
    height: 400px;
    background: var(--ink);
  }
  .card-front__panel {
    position: absolute;
    left: 3px;
    right: 3px;
    top: 45px;
    height: 230px;
    background: var(--paper);
  }
  .club-mark {
    position: absolute;
    left: 50%;
    top: 40px;
    width: 90px;
    height: 90px;
    margin-left: -45px;
    border-radius: 50%;
    background: var(--club-red);
  }
  .club-name {
    position: absolute;
    left: 0;
    right: 0;
    top: 146px;
    margin: 0;
    text-align: center;
    font-family: var(--serif);
    font-weight: 500;
    font-size: 46px;
    line-height: 1;
    letter-spacing: 0.5px;
    text-transform: uppercase;
    color: var(--club-red);
  }
  .name-field {
    position: absolute;
    left: 26px;
    top: 299px;
    width: 651px;
    height: 79px;
    background: var(--paper);
  }
  .name-note {
    position: absolute;
    left: 822px;
    top: 355px;
    margin: 0;
    font-size: 24px;
    line-height: 1;
    color: var(--ink);
  }

  /* Card back */
  .card-back {
    position: absolute;
    left: 74px;
    top: 516px;
    width: 700px;
    height: 401px;
    box-sizing: border-box;
    border: 2px solid var(--ink);
    background: var(--paper);
  }
  .divider {
    position: absolute;
    top: 92px;
    height: 6px;
    background: var(--ink);
  }
  .divider--left { left: 0; width: 302px; }
  .divider--right { left: 402px; right: 0; }
  .emblem {
    position: absolute;
    left: 297px;
    top: 18px;
    width: 110px;
    height: 110px;
    border-radius: 50%;
    background: radial-gradient(circle, var(--emblem-red) 0%, var(--emblem-red) 55%, var(--emblem-deep) 100%);
  }
  .member-number {
    position: absolute;
    left: 50px;
    top: 200px;
    margin: 0;
    font-size: 27px;
    line-height: 1.2;
    color: var(--ink);
    display: flex;
    align-items: baseline;
    gap: 8px;
  }
  .member-number__line {
    display: inline-block;
    width: 320px;
    border-bottom: 2px solid var(--ink);
  }
  .contact-band {
    position: absolute;
    left: 0;
    right: 0;
    bottom: 0;
    height: 127px;
    background: var(--ink);
    color: var(--paper);
    text-align: center;
    font-size: 24px;
    line-height: 41px;
    padding-top: 20px;
    box-sizing: border-box;
  }
  .contact-band p { margin: 0; }
</style>
</head>
<body>
<main class="sheet">

  <section class="card-front" aria-label="Membership card front">
    <div class="card-front__panel">
      <span class="club-mark" aria-hidden="true"></span>
      <h1 class="club-name">Maple Lantern Circle</h1>
    </div>
    <div class="name-field" aria-label="Space for member name"></div>
  </section>

  <p class="name-note">Place to write in their name</p>

  <section class="card-back" aria-label="Membership card back">
    <div class="divider divider--left"></div>
    <div class="divider divider--right"></div>
    <div class="emblem" role="img" aria-label="Red decorative emblem"></div>
    <p class="member-number">Membership Number: <span class="member-number__line"></span></p>
    <div class="contact-band">
      <p>www.friendspage.example/maplelantern.cir</p>
      <p>maplelanterncir@mailbox.example</p>
    </div>
  </section>

</main>
</body>
</html>
```